Re-Design the flow of the Keystride Principles

The keystride principle is a 10 step model that helps teams/organizations become high performing. Attached the model which i created. I love the design as it is but i used a template i don't owe the rights of so i would like to use this platform to see what you can come up with the redesign this flow while keeping the key elements in place. I like the flow, i like the cleanness and i like it to be compact.

Target Market(s)

Organizational change / Leadership/ Consultancy

Industry/Entity Type

Leadership

Requirements
Must have
• Keep as much as possible the flow and feel of the attached
Nice to have
• -Maybe some twist in how the different parts connect (not a must)
Should not have
• Less or more steps than added in the attached file

```html
<!DOCTYPE html>
<html lang="en">
<head>
<meta charset="utf-8">
<title>The Keystride Principles</title>
<link href="https://fonts.googleapis.com/css2?family=Barlow:wght@500;600;700;800&display=swap" rel="stylesheet">
<style>
  :root {
    --bg: #808080;
    --white: #ffffff;
    --ink: #595959;
    --sky: #2fb4e8;
    --royal: #0a6db5;
    --indigo: #4a59a8;
    --violet: #5b3c95;
    --teal: #4bbcc2;
    --lime: #9bc93c;
    --plum: #a0479a;
    --rose: #e8426e;
    --flame: #f05a28;
    --amber: #f6b91b;
  }
  html, body { margin: 0; padding: 0; overflow: hidden; background: var(--bg); }
  .canvas { width: 1200px; height: 1000px; display: block; background: var(--bg); }
  svg text { font-family: "Barlow", sans-serif; }
  .title { font-weight: 800; font-size: 70px; fill: var(--white); }
  .title .accent { fill: var(--sky); }
  .subtitle { font-weight: 700; font-size: 15px; fill: var(--white); letter-spacing: 2px; }
  .tier-label { font-weight: 700; font-size: 22px; fill: var(--white); letter-spacing: 3px; }
  .group-label { font-weight: 700; font-size: 17px; fill: var(--white); }
  .step { font-weight: 700; font-size: 14.5px; text-anchor: middle; }
  .card { fill: var(--white); }
  .track { fill: none; stroke: var(--white); stroke-width: 6; stroke-linejoin: round; stroke-linecap: round; }
  .chevron { fill: var(--white); }
  .restart-line { fill: none; stroke: var(--white); stroke-width: 3; }
  .restart { font-weight: 700; font-size: 11px; fill: var(--white); text-anchor: middle; letter-spacing: 1px; }
  .goal-title { font-weight: 700; font-size: 14.5px; fill: var(--ink); text-anchor: middle; }
  .goal-list { font-weight: 600; font-size: 8px; fill: var(--ink); }
  .badge { stroke: var(--bg); stroke-width: 5; }
  .icon { fill: var(--white); stroke: none; }
  .icon-line { fill: none; stroke: var(--white); stroke-width: 2.5; stroke-linecap: round; stroke-linejoin: round; }
</style>
</head>
<body>
<svg class="canvas" viewBox="0 0 1200 1000" xmlns="http://www.w3.org/2000/svg">
  <!-- Heading -->
  <text class="title" x="600" y="107" text-anchor="middle" textLength="960" lengthAdjust="spacingAndGlyphs">THE <tspan class="accent">KEYSTRIDE</tspan> PRINCIPLES</text>
  <text class="subtitle" x="600" y="138" text-anchor="middle" textLength="915" lengthAdjust="spacingAndGlyphs">LIBERATE THE WORKPLACE UNLEASHING VALUE THROUGH PURPOSE AT EVERY LEVEL OF SCALE</text>

  <!-- Stride track: rises tier by tier into the goal -->
  <path class="track" d="M157.5 810 H970 Q1010 810 1010 770 V600 Q1010 560 970 560 H70 Q30 560 30 520 V350 Q30 310 70 310 H1000"/>

  <!-- Direction chevrons -->
  <g class="chevrons">
    <polygon class="chevron" points="327,800 341,810 327,820"/>
    <polygon class="chevron" points="679,800 693,810 679,820"/>
    <polygon class="chevron" points="693,550 679,560 693,570"/>
    <polygon class="chevron" points="341,550 327,560 341,570"/>
    <polygon class="chevron" points="20,440 30,426 40,440"/>
    <polygon class="chevron" points="1000,690 1010,676 1020,690"/>
  </g>

  <!-- Loop back to the start -->
  <path class="restart-line" d="M1070 540 V930 H157.5 V886"/>
  <polygon fill="var(--white)" points="157.5,872 149,887 166,887"/>
  <text class="restart" x="600" y="920">(RE)START HERE</text>
  <text class="restart" x="600" y="950">(RE)INVENT HERE</text>

  <!-- Goal arrow -->
  <g class="goal">
    <polygon fill="var(--white)" points="1070,200 1155,330 1140,330 1140,540 1000,540 1000,330 985,330"/>
    <g fill="none" stroke="var(--ink)" stroke-width="2" stroke-linejoin="round">
      <polygon points="1054,264 1086,264 1094,276 1070,302 1046,276"/>
      <polyline points="1046,276 1094,276"/>
      <polyline points="1062,264 1058,276 1070,302 1082,276 1078,264"/>
    </g>
    <text class="goal-title" x="1070" y="356">Reaching</text>
    <text class="goal-title" x="1070" y="375">Full Potential of</text>
    <text class="goal-title" x="1070" y="394">People and</text>
    <text class="goal-title" x="1070" y="413">Organization</text>
    <g class="goal-list">
      <circle cx="1014" cy="441" r="1.6" fill="var(--ink)"/><text x="1020" y="444">Productivity Up To 800%</text>
      <circle cx="1014" cy="458" r="1.6" fill="var(--ink)"/><text x="1020" y="461">Employee Engagement &gt;90%</text>
      <circle cx="1014" cy="475" r="1.6" fill="var(--ink)"/><text x="1020" y="478">Max Discretionary Effort Gap</text>
      <circle cx="1014" cy="492" r="1.6" fill="var(--ink)"/><text x="1020" y="495">High Resilience To Change</text>
    </g>
  </g>

  <!-- Tier and group headings -->
  <text class="tier-label" x="60" y="205">UNLEASHED ENGAGEMENT</text>
  <polygon fill="var(--white)" points="372,190 384,197 372,204"/>
  <text class="group-label" x="960" y="205" text-anchor="end">Capabilities Maximizing Excellence</text>

  <text class="group-label" x="60" y="455">Capabilities Driving a Solid Foundation</text>
  <text class="tier-label" x="960" y="455" text-anchor="end">HUMAN EXPERIENCE</text>
  <polygon fill="var(--white)" points="718,440 706,447 718,454"/>

  <text class="tier-label" x="60" y="705">SELF DIRECTION</text>
  <polygon fill="var(--white)" points="276,690 288,697 276,704"/>

  <!-- Cards: tier 1 -->
  <g class="cards">
    <rect x="60" y="750" width="195" height="120" rx="12" fill="var(--lime)"/><rect class="card" x="60" y="750" width="195" height="113" rx="12"/>
    <rect x="412" y="750" width="195" height="120" rx="12" fill="var(--teal)"/><rect class="card" x="412" y="750" width="195" height="113" rx="12"/>
    <rect x="765" y="750" width="195" height="120" rx="12" fill="var(--sky)"/><rect class="card" x="765" y="750" width="195" height="113" rx="12"/>

    <rect x="765" y="500" width="195" height="120" rx="12" fill="var(--royal)"/><rect class="card" x="765" y="500" width="195" height="113" rx="12"/>
    <rect x="412" y="500" width="195" height="120" rx="12" fill="var(--indigo)"/><rect class="card" x="412" y="500" width="195" height="113" rx="12"/>
    <rect x="60" y="500" width="195" height="120" rx="12" fill="var(--violet)"/><rect class="card" x="60" y="500" width="195" height="113" rx="12"/>

    <rect x="60" y="250" width="195" height="120" rx="12" fill="var(--plum)"/><rect class="card" x="60" y="250" width="195" height="113" rx="12"/>
    <rect x="295" y="250" width="195" height="120" rx="12" fill="var(--rose)"/><rect class="card" x="295" y="250" width="195" height="113" rx="12"/>
    <rect x="530" y="250" width="195" height="120" rx="12" fill="var(--flame)"/><rect class="card" x="530" y="250" width="195" height="113" rx="12"/>
    <rect x="765" y="250" width="195" height="120" rx="12" fill="var(--amber)"/><rect class="card" x="765" y="250" width="195" height="113" rx="12"/>
  </g>

  <!-- Icon badges -->
  <g class="badges">
    <circle class="badge" cx="157.5" cy="750" r="28" fill="var(--lime)"/>
    <circle class="badge" cx="509.5" cy="750" r="28" fill="var(--teal)"/>
    <circle class="badge" cx="862.5" cy="750" r="28" fill="var(--sky)"/>
    <circle class="badge" cx="862.5" cy="500" r="28" fill="var(--royal)"/>
    <circle class="badge" cx="509.5" cy="500" r="28" fill="var(--indigo)"/>
    <circle class="badge" cx="157.5" cy="500" r="28" fill="var(--violet)"/>
    <circle class="badge" cx="157.5" cy="250" r="28" fill="var(--plum)"/>
    <circle class="badge" cx="392.5" cy="250" r="28" fill="var(--rose)"/>
    <circle class="badge" cx="627.5" cy="250" r="28" fill="var(--flame)"/>
    <circle class="badge" cx="862.5" cy="250" r="28" fill="var(--amber)"/>
  </g>

  <!-- Icons -->
  <g class="icon-purpose" transform="translate(157.5 751)">
    <path class="icon" d="M0 13 C-16 2 -17 -9 -9 -12 C-4 -14 -1 -10 0 -7 C1 -10 4 -14 9 -12 C17 -9 16 2 0 13 Z"/>
    <path fill="none" stroke="var(--lime)" stroke-width="2" stroke-linejoin="round" d="M-13 -1 H-6 L-3 -7 L1 5 L4 -1 H13"/>
  </g>
  <g class="icon-vision" transform="translate(511 748)">
    <rect class="icon" x="-16" y="-5" width="28" height="8" rx="2" transform="rotate(-25)"/>
    <path class="icon-line" d="M-1 2 L-8 15 M-1 2 L6 15 M-1 2 V15"/>
  </g>
  <g class="icon-strategy" transform="translate(862.5 750)">
    <circle class="icon-line" r="11"/><circle class="icon-line" r="5"/><circle class="icon" r="1.8"/>
    <path class="icon-line" d="M0 -16 V-8 M0 8 V16 M-16 0 H-8 M8 0 H16"/>
  </g>
  <g class="icon-safety" transform="translate(862.5 500)">
    <circle class="icon" cx="-9" cy="-10" r="3.5"/><circle class="icon" cx="0" cy="-10" r="3.5"/><circle class="icon" cx="9" cy="-10" r="3.5"/>
    <rect class="icon" x="-13" y="-5" width="7" height="13" rx="2"/><rect class="icon" x="-3.5" y="-5" width="7" height="13" rx="2"/><rect class="icon" x="6" y="-5" width="7" height="13" rx="2"/>
    <path class="icon-line" d="M-11 9 V15 M-8 9 V15 M-1.5 9 V15 M1.5 9 V15 M8 9 V15 M11 9 V15" stroke-width="1.8"/>
  </g>
  <g class="icon-motivation" transform="translate(509.5 501)">
    <path class="icon" d="M0 13 C-16 2 -17 -9 -9 -12 C-4 -14 -1 -10 0 -7 C1 -10 4 -14 9 -12 C17 -9 16 2 0 13 Z"/>
    <path fill="none" stroke="var(--indigo)" stroke-width="2" stroke-linejoin="round" d="M-13 -1 H-6 L-3 -7 L1 5 L4 -1 H13"/>
  </g>
  <g class="icon-growth" transform="translate(157.5 501)">
    <circle class="icon" cx="-10" cy="-8" r="3"/><circle class="icon" cx="-2" cy="-10" r="3"/><circle class="icon" cx="6" cy="-8" r="3"/>
    <rect class="icon" x="-14" y="-4" width="24" height="7" rx="2"/>
    <path class="icon-line" d="M-14 12 L-4 6 L2 9 L12 1"/><path class="icon" d="M8 -1 L15 -2 L13 5 Z"/>
  </g>
  <g class="icon-feedback" transform="translate(157.5 250)">
    <circle class="icon-line" r="8"/><circle class="icon" r="3"/>
    <path class="icon-line" d="M0 -13 V-9 M0 9 V13 M-13 0 H-9 M9 0 H13 M-9 -9 L-6.5 -6.5 M6.5 6.5 L9 9 M9 -9 L6.5 -6.5 M-6.5 6.5 L-9 9"/>
  </g>
  <g class="icon-community" transform="translate(392.5 250)">
    <path class="icon-line" d="M0 -14 V-4 M0 4 V14 M-14 0 H-4 M4 0 H14"/>
    <circle class="icon" cx="0" cy="-14" r="3"/><circle class="icon" cx="0" cy="14" r="3"/><circle class="icon" cx="-14" cy="0" r="3"/><circle class="icon" cx="14" cy="0" r="3"/>
    <circle class="icon" r="3.5"/>
  </g>
  <g class="icon-trophy" transform="translate(627.5 250)">
    <path class="icon" d="M-9 -13 H9 V-3 C9 4 4 7 0 7 C-4 7 -9 4 -9 -3 Z"/>
    <path class="icon-line" d="M-9 -10 H-14 C-14 -3 -11 0 -8 0 M9 -10 H14 C14 -3 11 0 8 0"/>
    <rect class="icon" x="-2" y="6" width="4" height="6"/><rect class="icon" x="-8" y="11" width="16" height="4" rx="1"/>
  </g>
  <g class="icon-monitor" transform="translate(864 251)">
    <circle class="icon-line" cx="-3" cy="-3" r="10" stroke-width="3"/>
    <path class="icon-line" d="M4 4 L12 12" stroke-width="4.5"/>
    <path class="icon-line" d="M-10 -3 H-7 L-5 -7 L-2 2 L1 -3 H4" stroke-width="1.8"/>
  </g>

  <!-- Step labels -->
  <text class="step" fill="var(--lime)"><tspan x="157.5" y="806">Discover Your</tspan><tspan x="157.5" y="824">Purpose.</tspan><tspan x="157.5" y="842">Why Do You Exist?</tspan></text>
  <text class="step" fill="var(--teal)"><tspan x="509.5" y="800">Indentify</tspan><tspan x="509.5" y="818">Purpose</tspan><tspan x="509.5" y="836">Activators</tspan><tspan x="509.5" y="854">(Vision)</tspan></text>
  <text class="step" fill="var(--sky)"><tspan x="862.5" y="806">Develop a</tspan><tspan x="862.5" y="824">Master Plan</tspan><tspan x="862.5" y="842">(Strategy)</tspan></text>

  <text class="step" fill="var(--royal)"><tspan x="862.5" y="550">Cultivate</tspan><tspan x="862.5" y="568">Psychological</tspan><tspan x="862.5" y="586">Safety and</tspan><tspan x="862.5" y="604">Ownership</tspan></text>
  <text class="step" fill="var(--indigo)"><tspan x="509.5" y="550">Top Into Peoples</tspan><tspan x="509.5" y="568">Purpose and</tspan><tspan x="509.5" y="586">Passion</tspan><tspan x="509.5" y="604">(Instrinsic Motivation)</tspan></text>
  <text class="step" fill="var(--violet)"><tspan x="157.5" y="550">Unlock Culture</tspan><tspan x="157.5" y="568">Of Personal</tspan><tspan x="157.5" y="586">Growth &amp;</tspan><tspan x="157.5" y="604">Development</tspan></text>

  <text class="step" fill="var(--plum)"><tspan x="157.5" y="306">Prioritize</tspan><tspan x="157.5" y="324">Feedback &amp;</tspan><tspan x="157.5" y="342">Transparency</tspan></text>
  <text class="step" fill="var(--rose)"><tspan x="392.5" y="306">Empower The</tspan><tspan x="392.5" y="324">Community From</tspan><tspan x="392.5" y="342">Bottom-Up</tspan></text>
  <text class="step" fill="var(--flame)"><tspan x="627.5" y="306">Put Excellent (Team)</tspan><tspan x="627.5" y="324">Performance In</tspan><tspan x="627.5" y="342">The Spotlight</tspan></text>
  <text class="step" fill="var(--amber)"><tspan x="862.5" y="306">Monitor</tspan><tspan x="862.5" y="324">Engagement</tspan><tspan x="862.5" y="342">Realtime</tspan></text>
</svg>
</body>
</html>
```